Book Cover - The Velvet Lantern Almanac Collection

We are writing a book about the velvet lantern almanac collection, including Guerrilla Marketing. Advertising, Branding and PR.

We are looking for a fun and quirky cover, and are open to your ideas 💡
My website and social media are on www.TorvanPelica.co and posts are shared on Trelvano. Again we are open to ideas

```html
<!DOCTYPE html>
<html lang="en">
<head>
<meta charset="utf-8">
<title>The Velvet Lantern Almanac Collection — Book Cover</title>
<link rel="stylesheet" href="https://fonts.googleapis.com/css2?family=Barlow+Condensed:wght@500;600;700&family=Barlow:wght@700&display=swap">
<style>
  :root {
    --page: #ffffff;
    --cover: #000000;
    --ink: #ffffff;
    --gold: #f8bf38;
    --amber: #f2a10f;
    --amber-deep: #8c5a00;
  }
  html, body {
    margin: 0;
    padding: 0;
    width: 1200px;
    height: 1200px;
    overflow: hidden;
    background: var(--page);
  }
  .canvas {
    position: relative;
    width: 1200px;
    height: 1200px;
    background: var(--page);
  }
  .book-cover {
    position: absolute;
    left: 265px;
    top: 96px;
    width: 670px;
    height: 1008px;
    background: var(--cover);
    overflow: hidden;
  }
  .cover-art {
    position: absolute;
    inset: 0;
    width: 670px;
    height: 1008px;
    display: block;
  }
  .title-line {
    font-family: "Barlow Condensed", sans-serif;
    fill: var(--ink);
    text-anchor: middle;
  }
  .title-the { font-weight: 500; font-size: 74px; }
  .title-velvet { font-weight: 500; font-size: 126px; }
  .title-lantern { font-weight: 700; font-size: 132px; fill: var(--gold); }
  .title-almanac { font-weight: 500; font-size: 292px; }
  .stamp-word {
    font-family: "Barlow Condensed", sans-serif;
    font-weight: 600;
    font-size: 80px;
    fill: var(--ink);
    text-anchor: middle;
  }
  .stamp { filter: drop-shadow(0 0 10px rgba(248, 191, 56, 0.85)) drop-shadow(0 0 24px rgba(242, 161, 15, 0.6)); }
  .rule { stroke: var(--ink); stroke-width: 2.5; }
  .author {
    position: absolute;
    left: 0;
    right: 0;
    top: 937px;
    margin: 0;
    text-align: center;
    font-family: "Barlow", sans-serif;
    font-weight: 700;
    font-size: 23px;
    letter-spacing: 0.32em;
    padding-left: 0.32em;
    color: var(--ink);
    line-height: 1;
  }
</style>
</head>
<body>
<main class="canvas">
  <section class="book-cover" aria-label="Book cover: The Velvet Lantern Almanac Collection by Dara Quillfenn">
    <svg class="cover-art" viewBox="0 0 670 1008" xmlns="http://www.w3.org/2000/svg">
      <defs>
        <linearGradient id="art-fill" x1="0" y1="0" x2="0" y2="1">
          <stop offset="0%" stop-color="#1a1a1a"/>
          <stop offset="45%" stop-color="#8c5a00"/>
          <stop offset="100%" stop-color="#f2a10f" stop-opacity="0.55"/>
        </linearGradient>
        <linearGradient id="stamp-fill" x1="0" y1="0" x2="0" y2="1">
          <stop offset="0%" stop-color="#c98a0c"/>
          <stop offset="100%" stop-color="#8c5a00"/>
        </linearGradient>
        <radialGradient id="stamp-halo" cx="50%" cy="50%" r="50%">
          <stop offset="0%" stop-color="#f8bf38" stop-opacity="0.35"/>
          <stop offset="100%" stop-color="#f8bf38" stop-opacity="0"/>
        </radialGradient>
      </defs>

      <rect class="lamp-illustration" x="252" y="0" width="176" height="258"
            fill="url(#art-fill)" role="img" aria-label="Illustration area: a glowing yellow light bulb hanging from a cord with short light rays around it"/>

      <line class="rule" x1="104" y1="301" x2="275" y2="301"/>
      <line class="rule" x1="406" y1="301" x2="577" y2="301"/>
      <text class="title-line title-the" x="340" y="329" textLength="80" lengthAdjust="spacingAndGlyphs">THE</text>
      <text class="title-line title-velvet" x="338" y="439" textLength="475" lengthAdjust="spacing">VELVET</text>
      <text class="title-line title-lantern" x="340" y="551" textLength="486" lengthAdjust="spacingAndGlyphs">LANTERN</text>
      <text class="title-line title-almanac" x="338" y="772" textLength="476" lengthAdjust="spacingAndGlyphs">ALMANAC</text>

      <line class="rule" x1="96" y1="820" x2="568" y2="820"/>

      <ellipse cx="340" cy="808" rx="230" ry="120" fill="url(#stamp-halo)"/>
      <g class="stamp" transform="translate(340 810) rotate(-12)">
        <rect x="-168" y="-54" width="336" height="108" fill="url(#stamp-fill)"/>
        <rect x="-158" y="-44" width="316" height="88" fill="none" stroke="var(--ink)" stroke-width="4"/>
        <text class="stamp-word" x="0" y="28" textLength="280" lengthAdjust="spacingAndGlyphs">COLLECTION</text>
      </g>
    </svg>
    <p class="author">DARA QUILLFENN</p>
  </section>
</main>
</body>
</html>
```